QSL Card

project is a QSL card for amateur radio operators - must radio show call sign predomiately and in large letters on the card - VK5RUT - then must say somewhere Greetings from Australia - must also include name, address, website and coordinates in small trype - Martin Keble,47 Birch Rd., Tarrowby SA 5170 Australia, http://www.martinkebleqsl.com, - Grid Square PF82kr, CQ Zone 30, ITU Zone 59 - must also have a long rectangular box down the bottom of the card with six boxes inside the long box that can be filled in showing a heading in each box --- in box 1 Confirming QSO with.... box 2 Date (Z) ....., box 3 UTC ...... box 4 Freq / 2XMode ...... box 5 Pwr Out,..... boxx 6 Report ..... use attached pictures in the design with the radio equiipment as a background and my photo superimposed somewhere -- and the other attached image shows how i want the box to look - and on the right hand side down the bottom in small letters - 73s, Tnx QSL Pse

Reason: none of the designs i received totally fit the bill - see my new brief and budget

hi all - i finally decided i didnt like any of the designs i received so i have increased the budget and extended the deadline - i have also updated my brief and added another picture

Target Market(s)

amateur radio operators

Industry/Entity Type

Radio

Colors

Designer to choose colors to be used in the design.

```html
<!DOCTYPE html>
<html lang="en">
<head>
<meta charset="utf-8">
<title>QSL Card – VK5RUT Martin Keble</title>
<link rel="stylesheet" href="https://fonts.googleapis.com/css2?family=Lato:wght@400;700;900&display=swap">
<style>
  :root{
    --page:#eeeae4;
    --photo-dark:#2e2c2a;
    --photo-mid:#5d5a55;
    --photo-light:#8a857c;
    --panel:rgba(41,160,214,.9);
    --panel-edge:#1d7fb0;
    --strip:#111316;
    --white:#ffffff;
    --title-shadow:rgba(0,40,70,.55);
    --text-shadow:rgba(0,0,0,.6);
  }
  *{box-sizing:border-box;margin:0;padding:0}
  html,body{width:1200px;height:937px;overflow:hidden;background:var(--page)}
  body{position:relative;font-family:'Lato',sans-serif;color:var(--white)}
  .card{position:absolute;left:59px;top:50px;width:1084px;height:837px;overflow:hidden;
    box-shadow:0 6px 18px rgba(0,0,0,.35)}
  .card__photo{position:absolute;inset:0;
    background:
      radial-gradient(ellipse at 30% 55%, var(--photo-light) 0%, transparent 55%),
      linear-gradient(160deg, var(--photo-mid) 0%, var(--photo-dark) 75%)}
  .card__edge{position:absolute;left:0;top:0;width:22px;height:100%;
    background:linear-gradient(90deg,rgba(0,0,0,.65),rgba(0,0,0,0))}

  .station{position:absolute;left:40px;top:40px;width:440px;text-shadow:2px 3px 5px var(--text-shadow)}
  .station__call{font-weight:900;font-size:104px;line-height:1;letter-spacing:2px}
  .station__greeting{font-weight:700;font-size:26px;margin-top:8px}
  .station__grid{position:absolute;left:40px;bottom:30px;font-size:17px;line-height:24px;
    text-shadow:1px 2px 4px var(--text-shadow)}

  .panel{position:absolute;left:490px;top:0;width:500px;height:100%;background:var(--panel);
    border-left:2px solid var(--panel-edge)}
  .panel__title{position:absolute;left:0;right:0;top:40px;text-align:center;
    font-weight:900;font-size:62px;line-height:80px;letter-spacing:1px;font-variant:small-caps;
    text-shadow:2px 3px 4px var(--title-shadow)}
  .panel__rule{position:absolute;left:38px;top:152px;width:422px;height:2px;background:var(--white)}
  .log{position:absolute;left:14px;top:235px;list-style:none}
  .log__field{font-weight:700;font-size:23px;height:66px;line-height:28px}
  .contact{position:absolute;left:0;right:0;text-align:center;font-size:25px;line-height:34px}
  .contact--address{top:662px}
  .contact--web{top:752px}
  .contact svg{vertical-align:-4px;margin-right:6px}
  .panel__sign-off{position:absolute;right:16px;bottom:10px;font-size:15px;font-weight:700}

  .strip{position:absolute;left:990px;top:0;width:94px;height:100%;background:var(--strip)}
  .strip__call{position:absolute;left:47px;top:165px;transform-origin:0 0;transform:rotate(90deg) translateY(-50%);
    white-space:nowrap;font-weight:900;font-size:41px;display:flex;align-items:center;gap:12px}
  .strip__call svg{transform:rotate(-90deg)}
</style>
</head>
<body>
  <section class="card">
    <div class="card__photo" role="img" aria-label="Background photograph of the operator's amateur radio station: transceivers, power supply, clock, monitor and keyboard, with the operator's portrait and QSL cards on the wall"></div>
    <div class="card__edge"></div>

    <div class="station">
      <p class="station__call">VK5RUT</p>
      <p class="station__greeting">Greetings from Australia</p>
    </div>
    <p class="station__grid">Grid Square PF82kr<br>CQ Zone 30 &nbsp;·&nbsp; ITU Zone 59</p>

    <div class="panel">
      <h1 class="panel__title">Martin Keble</h1>
      <div class="panel__rule"></div>
      <ul class="log">
        <li class="log__field">Confirming QSO with :</li>
        <li class="log__field">Date (Z) :</li>
        <li class="log__field">UTCZ :</li>
        <li class="log__field">Freq / 2XMode :</li>
        <li class="log__field">Pwr Out :</li>
        <li class="log__field">Report :</li>
      </ul>
      <p class="contact contact--address">
        <svg width="20" height="26" viewBox="0 0 20 26"><path d="M10 0C4.5 0 0 4.4 0 9.8 0 17 10 26 10 26s10-9 10-16.2C20 4.4 15.5 0 10 0zm0 14a4.2 4.2 0 1 1 0-8.4 4.2 4.2 0 0 1 0 8.4z" fill="#fff"/></svg>47 Birch Rd., Tarrowby SA 5170<br>Australia
      </p>
      <p class="contact contact--web">
        <svg width="24" height="24" viewBox="0 0 24 24" fill="none" stroke="#fff" stroke-width="2"><circle cx="12" cy="12" r="10"/><ellipse cx="12" cy="12" rx="4.5" ry="10"/><path d="M2 12h20M4 6.5h16M4 17.5h16"/></svg>www.martinkebleqsl.com
      </p>
      <p class="panel__sign-off">73s, Tnx QSL Pse</p>
    </div>

    <aside class="strip">
      <div class="strip__call">
        <svg width="34" height="34" viewBox="0 0 34 34"><circle cx="17" cy="17" r="15" fill="none" stroke="#fff" stroke-width="2.5"/><path d="M12 9c1-.6 2 0 2.4.8l1.3 2.6c.4.8.1 1.6-.5 2l-1 .7c.9 2 2.4 3.6 4.4 4.6l.8-1c.5-.6 1.300-.8 2-.4l2.6 1.4c.8.4 1.2 1.4.6 2.3-1 1.6-2.6 2.4-4.4 1.8C14.6 22.4 11 18.6 9.8 14c-.5-1.9.5-3.9 2.2-5z" fill="#fff"/></svg>
        <span>Call Today : 08 8145-2967</span>
      </div>
    </aside>
  </section>
</body>
</html>
```